Yoga By Marisol Ad for print

I need a print ad designed to go in a brochure for a charity event. I've attached the specs. I need the specs for the 1/2 page ad.
Text for ad:

“E-RYT 200 extensive training with Asana Scholars
Social Media Influencer
Offering group, private and corporate yoga classes
Email: info@yogabymarisol-studio.com
Web: www.yogabymarisol-studio.com
Phone: 480-555-0163
Instagram: @flowofmarisol

Target Market(s)

Yoga practitioners and businesses looking to bring yoga in to their operation.

Font styles to use
Serif
Script

Colors
eda3c7
e34197
eea4c8
f9d9e8
feeeee
000000
1b1b1b
cbcbcb
eaeaea

Requirements
Must have
• One version of my logo, I have provided many to choose from for best aesthetic appeal

```html
<!DOCTYPE html>
<html lang="en">
<head>
<meta charset="utf-8">
<title>Yoga By Marisol – Half Page Ad</title>
<link href="https://fonts.googleapis.com/css2?family=EB+Garamond:wght@400;500&display=swap" rel="stylesheet">
<style>
  :root {
    --pink-soft: #eda3c7;
    --magenta: #e34197;
    --pink: #eea4c8;
    --blush: #f9d9e8;
    --cream: #feeeee;
    --black: #000000;
    --ink: #1b1b1b;
    --grey: #cbcbcb;
    --mist: #eaeaea;
    --plum: #5b1d3f;
    --white: #ffffff;
  }
  * { margin: 0; padding: 0; box-sizing: border-box; }
  html, body { width: 864px; height: 1200px; overflow: hidden; background: var(--white); }
  .ad {
    position: relative;
    width: 864px;
    height: 1200px;
    overflow: hidden;
    font-family: "EB Garamond", Georgia, serif;
    color: var(--ink);
  }
  .backdrop {
    position: absolute;
    left: 0; top: 0;
    width: 704px; height: 1200px;
    background: linear-gradient(to right, var(--pink-soft) 0%, var(--pink) 25%, var(--blush) 60%, var(--pink) 100%);
  }
  .portrait {
    position: absolute;
    left: 704px; top: 0;
    width: 160px; height: 1200px;
    background: linear-gradient(to bottom, #ffffff 0%, #e6e6e6 30%, #d4d4d4 60%, #e2e2e2 100%);
  }
  .panel {
    position: absolute;
    left: 126px; top: 92px;
    width: 558px; height: 1048px;
    background: rgba(254, 238, 238, 0.82);
  }
  .brand { position: absolute; left: 0; width: 812px; top: 122px; text-align: center; }
  .brand-mark {
    display: block;
    width: 48px; height: 48px;
    margin: 0 auto 22px;
    border-radius: 50%;
    background: var(--ink);
  }
  .brand-name { font-size: 58px; font-weight: 500; color: var(--ink); line-height: 1; }
  .content { position: absolute; left: 0; top: 0; width: 812px; text-align: center; }
  .line { position: absolute; left: 0; width: 812px; white-space: nowrap; line-height: 1; }
  .credential { top: 373px; font-size: 56px; }
  .training, .offer { font-size: 44px; }
  .influencer { font-size: 44px; color: var(--plum); }
  .contact { font-size: 35px; }
  .contact .value { color: var(--plum); }
</style>
</head>
<body>
<div class="ad">
  <div class="backdrop" role="img" aria-label="Soft pink and magenta striped backdrop"></div>
  <div class="portrait" role="img" aria-label="Black and white photo of the instructor seated cross-legged, one arm stretched overhead"></div>
  <div class="panel"></div>

  <div class="brand">
    <span class="brand-mark"></span>
    <div class="brand-name">Serene Stride</div>
  </div>

  <div class="content">
    <div class="line credential">E-RYT 200</div>
    <div class="line training" style="top:486px">Extensive training with</div>
    <div class="line training" style="top:531px">Asana Scholars</div>
    <div class="line influencer" style="top:620px">Social Media Influencer</div>
    <div class="line offer" style="top:664px">Offering group, private and</div>
    <div class="line offer" style="top:709px">corporate yoga classes</div>
    <div class="line contact" style="top:849px">Email: <span class="value">info@yogabymarisol-studio.com</span></div>
    <div class="line contact" style="top:895px">Web: <span class="value">www.yogabymarisol-studio.com</span></div>
    <div class="line contact" style="top:939px">Phone: <span class="value">480-555-0163</span></div>
    <div class="line contact" style="top:984px">Instagram: <span class="value">@flowofmarisol</span></div>
  </div>
</div>
</body>
</html>
```